Re-brand our business and design!

We need a simple informational website (editable for in the future use)
We need our logo(we have included logo), name, who we are, and what we do displayed.

This is our current site (which is not acceptable, and only a template site): all our information is on this site, please use it forreferanceofinformation.
Www.brightlanefixers.com

Target Market(s)

Real estate brokers, and realtors,homeowners, and anyone looking for home repairs.

Industry/Entity Type

Business

Number of Pages Required

4 page

Font styles to use
Sans Serif

Requirements
Must have
• Our name, contact info, services, and our logo (which we will Email upon request)
• MUST have originality to the site.
• custom "contact us form" or request an estimate form.
Nice to have
• page for real customer testimonies.
• page for our previous work where we can upload pics of completed jobs.
Should not have
• any infringements on any copyrights or plagiarism at all.

```html
<!DOCTYPE html>
<html lang="en">
<head>
<meta charset="utf-8">
<title>Bright Lane Fixers — Home Repairs and Maintenance</title>
<link href="https://fonts.googleapis.com/css2?family=Lato:wght@300;400;700&display=swap" rel="stylesheet">
<style>
:root{
  --red:#e00000;
  --red-dark:#b80000;
  --ink:#1a1a1a;
  --text:#333;
  --muted:#8a8a8a;
  --header-bg:#ededed;
  --tile:#8c8c8c;
  --tile-dark:#6e6e6e;
  --footer:#2b2b2b;
  --white:#fff;
}
*{box-sizing:border-box;margin:0;padding:0}
html,body{width:1200px;height:2244px;overflow:hidden}
body{font-family:"Lato",Arial,sans-serif;color:var(--text);background:var(--white);position:relative}
.abs{position:absolute}

/* top bar */
.topbar{left:0;top:0;width:1200px;height:33px;background:var(--white);font-size:13px;color:var(--text)}
.topbar .welcome{left:172px;top:8px}
.topbar .phone{left:745px;top:6px;display:flex;align-items:center;gap:9px}
.topbar .touch{left:903px;top:8px}
.social{top:5px;width:21px;height:21px;border-radius:50%;background:var(--red)}

/* header */
.header{left:0;top:33px;width:1200px;height:96px;background:var(--header-bg)}
.brand{left:172px;top:34px;display:flex;align-items:center;gap:10px;font-weight:700;font-size:19px;color:var(--ink)}
.brand-mark{width:18px;height:18px;background:var(--red)}
.nav a{position:absolute;top:40px;font-size:13px;color:var(--ink);text-decoration:none}
.nav .current{left:687px;top:34px;width:58px;height:27px;border:1px solid var(--red);color:var(--red);display:flex;align-items:center;justify-content:center}

/* hero */
.hero{left:0;top:129px;width:1200px;height:480px;background:linear-gradient(180deg,#8fa7b8 0%,#7b6b5c 35%,#7a5848 60%,#4f6a3a 88%,#3d5a2a 100%)}
.hero-panel{left:404px;top:95px;width:553px;height:307px;background:rgba(30,30,30,.55)}
.hero h1{left:495px;top:117px;font-weight:400;font-size:44px;color:var(--white)}
.hero p{left:495px;top:178px;width:430px;font-size:16px;line-height:21px;color:var(--white)}
.btn{background:var(--red);color:var(--white);font-weight:700;display:flex;align-items:center;justify-content:center;border-radius:3px}
.hero .learn{left:494px;top:312px;width:121px;height:33px;font-size:17px}
.dots{left:574px;top:452px;display:flex;gap:6px}
.dots span{width:9px;height:9px;border-radius:50%;background:#ddd}
.dots .on{background:var(--red)}

/* services */
.offer-kicker{left:0;top:644px;width:1200px;text-align:center;font-weight:300;font-size:30px;color:var(--muted)}
.offer-title{left:0;top:683px;width:1200px;text-align:center;font-weight:700;font-size:32px;color:var(--ink)}
.services{left:278px;top:755px;width:644px;height:428px;display:grid;grid-template-columns:repeat(3,213px);grid-template-rows:repeat(2,213px);gap:2px}
.service{background:linear-gradient(180deg,var(--tile),var(--tile-dark));display:flex;flex-direction:column;align-items:center;justify-content:center;gap:16px;color:var(--white);font-size:14px}
.service.active{background:linear-gradient(180deg,var(--red),var(--red-dark))}
.service svg{width:56px;height:56px}
.see-all{left:542px;top:1219px;width:118px;height:45px;font-size:15px;font-weight:400}

/* about */
.about-title{left:172px;top:1340px;font-weight:300;font-size:40px;color:var(--ink)}
.about-title b{font-weight:700}
.about-text{left:172px;top:1404px;width:610px;font-size:13.4px;line-height:24px;color:var(--muted)}
.about-photo{left:778px;top:1306px;width:299px;height:298px;background:linear-gradient(180deg,#e8d6c6 0%,#c9c9c9 30%,#3b4fc2 55%,#2a3ba4 100%);border-radius:140px 140px 0 0}

/* contact */
.contact{left:0;top:1604px;width:1200px;height:577px;background:linear-gradient(180deg,#8a8a8a 0%,#7d7f80 50%,#6f7274 100%)}
.contact h2{left:172px;top:56px;font-weight:300;font-size:40px;color:var(--white)}
.contact h2 b{font-weight:700}
.contact .info{left:172px;font-size:14px;color:var(--white);display:flex;align-items:center;gap:10px}
.map{left:172px;top:251px;width:428px;height:251px;background:linear-gradient(135deg,#ebe7df,#d9d4c9)}
.form-intro{left:639px;top:60px;font-size:16.5px;line-height:22px;color:var(--white)}
.field-label{left:639px;font-size:13px;color:var(--white)}
.field{left:639px;width:390px;background:var(--white);border:1px solid #ccc}
.submit{left:639px;top:460px;width:119px;height:44px;font-size:15px}

/* footer */
.footer{left:0;top:2181px;width:1200px;height:63px;background:var(--footer);color:var(--white);font-size:12px}
.footer .links{left:173px;top:25px;word-spacing:2px}
.footer .copy{left:610px;top:26px;font-size:11px}
.footer .copy em{font-style:normal;color:var(--red)}
</style>
</head>
<body>

<div class="abs topbar">
  <span class="abs welcome">Welcome to Bright Lane Fixers</span>
  <span class="abs phone">
    <svg width="18" height="18" viewBox="0 0 20 20"><circle cx="10" cy="10" r="9" fill="none" stroke="#1a1a1a" stroke-width="1.6"/><path d="M7 5.5l1.6 2.4-1 1.2c.6 1.2 1.4 2 2.4 2.6l1.2-1 2.4 1.6-.8 1.8c-3.4-.2-6.4-3.4-6.6-6.8z" fill="#1a1a1a"/></svg>
    555-014-2276
  </span>
  <span class="abs touch">Get In Touch :</span>
  <span class="abs social" style="left:983px"></span>
  <span class="abs social" style="left:1008px"></span>
</div>

<header class="abs header">
  <div class="abs brand"><span class="brand-mark"></span>Bright Lane Fixers</div>
  <nav class="nav">
    <a class="current" href="#">Home</a>
    <a href="#" style="left:772px">Our Services</a>
    <a href="#" style="left:881px">About Us</a>
    <a href="#" style="left:969px">Contact Us</a>
  </nav>
</header>

<section class="abs hero" role="img" aria-label="Brick family house with a smiling repairman in a hard hat giving a thumbs up">
  <div class="abs hero-panel"></div>
  <h1 class="abs">We Build Your Dream</h1>
  <p class="abs">Looking for someone to help get your listing ready to show? A complete Home Repair Solution? Did an inspection reveal repairs needed before closing? Bright Lane Fixers can help!</p>
  <div class="abs btn learn">Learn More</div>
  <div class="abs dots"><span></span><span class="on"></span><span></span><span></span><span></span></div>
</section>

<div class="abs offer-kicker">HERE IS A SMALL TASTE OF</div>
<div class="abs offer-title">WHAT WE OFFER:</div>

<div class="abs services">
  <div class="service active">
    <svg viewBox="0 0 56 56"><path d="M8 44L40 12l6 6-32 32z" fill="#fff"/><rect x="40" y="6" width="10" height="14" rx="2" transform="rotate(45 45 13)" fill="#fff"/></svg>
    Carpentry
  </div>
  <div class="service">
    <svg viewBox="0 0 56 56"><rect x="6" y="14" width="30" height="10" fill="#fff"/><rect x="18" y="8" width="6" height="6" fill="#fff"/><rect x="12" y="5" width="18" height="4" fill="#fff"/><path d="M36 14h6v16h-6z" fill="#fff"/><path d="M39 36c-3 4-3 7 0 7s3-3 0-7z" fill="#fff"/></svg>
    Plumbing
  </div>
  <div class="service">
    <svg viewBox="0 0 56 56"><path d="M6 10l16 4v34L6 44z M50 10l-16 4v34l16-4z" fill="none" stroke="#fff" stroke-width="3"/><path d="M22 14h12" stroke="#fff" stroke-width="2"/></svg>
    Doors &amp; Windows
  </div>
  <div class="service">
    <svg viewBox="0 0 56 56"><circle cx="28" cy="28" r="20" fill="none" stroke="#fff" stroke-width="4"/><rect x="20" y="18" width="16" height="14" rx="3" fill="#fff"/><rect x="22" y="12" width="3" height="7" fill="#fff"/><rect x="31" y="12" width="3" height="7" fill="#fff"/><rect x="26" y="32" width="4" height="16" fill="#fff"/></svg>
    Electrical
  </div>
  <div class="service">
    <svg viewBox="0 0 56 56"><path d="M28 6L4 28h7v22h12V36h10v14h12V28h7z" fill="#fff"/></svg>
    Small Construction
  </div>
  <div class="service">
    <svg viewBox="0 0 56 56"><path d="M4 40L28 16l24 24" fill="none" stroke="#fff" stroke-width="4"/><rect x="38" y="16" width="5" height="10" fill="#fff"/></svg>
    Roofing Maintenance
  </div>
</div>

<div class="abs btn see-all">See All</div>

<h2 class="abs about-title">About <b>US</b></h2>
<p class="abs about-text">Imagine the feeling… you come home to find a fuse has blown and you can't get the kettle to work. Then comes that dreaded moment, "I guess i'll have to call an electrician" Now calling an electrician doesn't have to be a scary task. At Keystone Electrics we believe in what we do. And we do it with all our heart. Looking after our customers is our number one priority Combined with the highest standard for our installation work this results in a Beautiful bespoke service every single time.<br>But don't take it from us. Take a look for yourself…</p>
<div class="abs about-photo" role="img" aria-label="Smiling electrician in blue overalls carrying a coil of cable on his shoulder"></div>

<section class="abs contact" role="img" aria-label="Faded coastal landscape behind the contact area">
  <h2 class="abs">Contact <b>Information</b></h2>
  <div class="abs info" style="top:121px;width:380px;line-height:20px">Bright Lane Fixers , Your address-Harbor Ave 125, US 40217</div>
  <div class="abs info" style="top:172px">
    <svg width="18" height="18" viewBox="0 0 20 20"><circle cx="10" cy="10" r="9" fill="none" stroke="#fff" stroke-width="1.6"/><path d="M7 5.5l1.6 2.4-1 1.2c.6 1.2 1.4 2 2.4 2.6l1.2-1 2.4 1.6-.8 1.8c-3.4-.2-6.4-3.4-6.6-6.8z" fill="#fff"/></svg>
    555-014-2276
  </div>
  <div class="abs info" style="top:201px">
    <svg width="18" height="14" viewBox="0 0 18 14"><rect x="1" y="1" width="16" height="12" fill="none" stroke="#fff" stroke-width="1.5"/><path d="M1 1l8 7 8-7" fill="none" stroke="#fff" stroke-width="1.5"/></svg>
    dan@brightlanefixers.com
  </div>
  <div class="abs map" role="img" aria-label="Street map with a red pin marking the office location"></div>

  <p class="abs form-intro">Fill out the online request form<br>and we will get back to you to see how we can help.</p>
  <label class="abs field-label" style="top:129px">Name:</label>
  <div class="abs field" style="top:142px;height:37px"></div>
  <label class="abs field-label" style="top:204px">Email:</label>
  <div class="abs field" style="top:217px;height:36px"></div>
  <label class="abs field-label" style="top:279px">Message:</label>
  <div class="abs field" style="top:294px;height:134px"></div>
  <div class="abs btn submit">Submit</div>
</section>

<footer class="abs footer">
  <div class="abs links">Home &nbsp; / &nbsp; About Us &nbsp; / &nbsp; Our Services &nbsp; / &nbsp; Contact Us</div>
  <div class="abs copy">Copyright © 2016. <em>Bright Lane Fixers And Maintenance LLC.</em> &nbsp;| &nbsp;All rights reserved.</div>
</footer>

</body>
</html>
```